Crest Automotive Reconditioning Business Card

We need a professional business card that features our logo, a picture of the employee, and a brief list of our services.
I've attached a logo, and will attach photos at a later date.
The four services that need to be listed are Bumper repair and repainting, road rash repair, clear coat scratch repair, and automotive touch-up.
Target Market(s)
30 - 40 year male general managers of automobile dealerships. They are used to seeing every vendor gimmick under the sun. This brochure needs to impress with its simplicity and honesty.
Industry/Entity Type
Automotive
Look and feel
Each slider illustrates characteristics of the customer's brand and the style your logo design should communicate.

```html
<!DOCTYPE html>
<html lang="en">
<head>
<meta charset="utf-8">
<title>Crest Automotive Reconditioning – Business Card</title>
<link href="https://fonts.googleapis.com/css2?family=Open+Sans:wght@400;600;800&display=swap" rel="stylesheet">
<style>
  :root {
    --backdrop: #e9e6e2;
    --paper: #ffffff;
    --paper-shade: #eeeeee;
    --ink-dark: #3a3a3a;
    --panel-black: #131313;
    --panel-black-soft: #2a2a2a;
    --accent-orange: #ef6a26;
    --accent-orange-deep: #d9501a;
    --accent-orange-light: #f4874a;
    --brown-glow: #7a3a1c;
    --text-light: #f2f2f2;
    --photo-dark: #2b2623;
    --photo-mid: #6b5446;
  }
  * { margin: 0; padding: 0; box-sizing: border-box; }
  html, body {
    width: 1200px; height: 1023px; overflow: hidden;
    background: var(--backdrop);
    font-family: "Open Sans", Arial, sans-serif;
  }
  .canvas { position: relative; width: 1200px; height: 1023px; }

  .card {
    position: absolute; left: 330px; width: 540px; height: 308px;
    border-radius: 4px; overflow: hidden;
    box-shadow: 0 10px 28px rgba(0,0,0,.22);
  }
  .card--front { top: 120px; background: linear-gradient(180deg, var(--paper), var(--paper-shade)); }
  .card--back {
    top: 560px;
    background: radial-gradient(ellipse at 35% 40%, var(--accent-orange-light), var(--accent-orange) 55%, var(--accent-orange-deep));
  }

  .front-panel { position: absolute; left: 0; top: 0; width: 540px; height: 308px; }

  .employee-photo {
    position: absolute; right: 0; top: 0; width: 230px; height: 150px;
    background: linear-gradient(160deg, var(--photo-mid), var(--photo-dark) 70%);
  }

  .wordmark { position: absolute; color: var(--ink-dark); font-weight: 800; line-height: 1; }
  .wordmark__name { display: block; letter-spacing: 1px; }
  .wordmark__tag { display: block; letter-spacing: .5px; }
  .card--front .wordmark { left: 34px; top: 42px; }
  .card--front .wordmark__name { font-size: 50px; }
  .card--front .wordmark__tag { font-size: 12.5px; margin-top: 4px; }

  .contact { position: absolute; left: 34px; top: 192px; color: var(--text-light); }
  .contact__name { color: var(--accent-orange); font-size: 14px; line-height: 18px; font-weight: 600; letter-spacing: .5px; }
  .contact__role { font-size: 11px; line-height: 14px; margin-bottom: 5px; }
  .contact__row { display: flex; align-items: center; gap: 7px; font-size: 11px; line-height: 15px; }
  .contact__icon {
    width: 10px; height: 10px; border-radius: 2px; background: var(--accent-orange);
    display: flex; align-items: center; justify-content: center;
  }
  .contact__address {
    position: absolute; left: 34px; bottom: 12px; color: var(--accent-orange);
    font-size: 10.5px; line-height: 14px; letter-spacing: .6px;
  }

  .card--back .wordmark { left: 200px; top: 80px; color: #4a4a4a; }
  .card--back .wordmark__name { font-size: 74px; }
  .card--back .wordmark__tag { font-size: 17px; margin-top: 4px; }
  .services {
    position: absolute; left: 34px; bottom: 34px; color: var(--brown-glow);
    font-size: 11px; letter-spacing: .8px; line-height: 18px; text-transform: uppercase;
  }
</style>
</head>
<body>
<main class="canvas">

  <section class="card card--front" aria-label="Business card front">
    <svg class="front-panel" viewBox="0 0 540 308" aria-hidden="true">
      <defs>
        <linearGradient id="glow" x1="0" y1="0" x2="1" y2="0">
          <stop offset="0" stop-color="#7a3a1c" stop-opacity=".2"/>
          <stop offset=".6" stop-color="#7a3a1c"/>
          <stop offset="1" stop-color="#2a1a12"/>
        </linearGradient>
        <linearGradient id="blackpanel" x1="0" y1="0" x2="0" y2="1">
          <stop offset="0" stop-color="#2a2a2a"/>
          <stop offset="1" stop-color="#0e0e0e"/>
        </linearGradient>
      </defs>
      <path d="M0 172 C 160 166, 330 146, 540 124 L540 308 L0 308 Z" fill="url(#glow)"/>
      <path d="M0 182 C 170 176, 340 160, 540 146 L540 308 L0 308 Z" fill="url(#blackpanel)"/>
    </svg>

    <div class="employee-photo" role="img" aria-label="Portrait photograph of the employee in a dark suit"></div>

    <div class="wordmark">
      <span class="wordmark__name">CREST</span>
      <span class="wordmark__tag">AUTOMOTIVE RECONDITIONING</span>
    </div>

    <div class="contact">
      <p class="contact__name">DANIEL REYES</p>
      <p class="contact__role">Director</p>
      <p class="contact__row">
        <span class="contact__icon"><svg width="7" height="7" viewBox="0 0 10 10"><rect x="3" y="1" width="4" height="8" rx="1" fill="#fff"/></svg></span>
        9845310262
      </p>
      <p class="contact__row">
        <span class="contact__icon"><svg width="7" height="7" viewBox="0 0 10 10"><path d="M2 1 L4 1 L5 3 L4 4 Q5 6 6 6 L7 5 L9 6 L9 8 Q5 9 2 5 Q1 3 2 1Z" fill="#fff"/></svg></span>
        0836 2470518
      </p>
      <p class="contact__row">
        <span class="contact__icon"><svg width="7" height="7" viewBox="0 0 10 10"><rect x="1" y="2" width="8" height="6" fill="none" stroke="#fff" stroke-width="1.2"/><path d="M1 2 L5 5 L9 2" fill="none" stroke="#fff" stroke-width="1.2"/></svg></span>
        d.reyes@crestauto.in
      </p>
    </div>
    <p class="contact__address">F-4 LAKSHMI ARCADE, VIDYANAGAR, KARNATAKA, INDIA</p>
  </section>

  <section class="card card--back" aria-label="Business card back">
    <div class="wordmark">
      <span class="wordmark__name">CREST</span>
      <span class="wordmark__tag">AUTOMOTIVE RECONDITIONING</span>
    </div>
    <div class="services">
      <p>Bumper repair and repainting | Road rash repair</p>
      <p>Clear coat scratch repair | Automotive touch-up</p>
    </div>
  </section>

</main>
</body>
</html>
```